Tress Radiant from root to soul. Hair stylist that specializes in extensions.

I am Marisol I am a hair stylist and I would like a website designed for my hair business.

I currently book clients via my profile on glamslot.net/marisolbreck

I need a professional website ( tressradiantfromroottosoul.net ) to display photos and prices for services offered.

I would like to have a home page with a brief bio, Image with logo and testimonials at the bottom, and a header with tab that include: menu of services, gallery,and FAQs.

On the "Services" page, I'm not interested in photos on this page. Just the name of the service, brief description, and pricing. I would also like to have, on this page, "Appointment Request" with fields that include: Name, service requested, desired time frame (morning, afternoon, evening), and contact number and email

On the "Gallery" page, I would like pictures only, but arranged and/or presented in a creative way...

Target Market(s)

Women ages 25-55 who interested in hair extension services.

Industry/Entity Type

Hair And Beauty

Coding

Coded - Design and coding required

Number of Pages Required

5+ page

Font styles to use
Sans Serif

Requirements
Must have
• Must include tabs that include, Menu of services offered, a quik pae link to pay deposits with ease, location, contact information, photo gallery, and policy/faqs.
Nice to have
• If possible i would like to stream music with the ability to be silenced. I would like a neutral color palette tans and beige.
Should not have
• stock images

```html
<!DOCTYPE html>
<html lang="en">
<head>
<meta charset="utf-8">
<title>Tress Radiant from root to soul</title>
<link href="https://fonts.googleapis.com/css2?family=Raleway:wght@400;600;700&family=Open+Sans:wght@400;600&family=Italianno&display=swap" rel="stylesheet">
<style>
:root{
  --ink:#222428;
  --dark:#2b2d31;
  --darker:#1c1d20;
  --teal:#1fb39a;
  --teal-dark:#179480;
  --grey-bg:#f1f1f1;
  --line:#dcdcdc;
  --muted:#7a7a7a;
  --white:#ffffff;
  --tag:#e23b2e;
}
*{box-sizing:border-box;margin:0;padding:0}
html,body{width:1200px;height:2916px;overflow:hidden}
body{font-family:"Open Sans",Arial,sans-serif;color:var(--ink);background:var(--white);position:relative}
.topbar{height:28px;background:var(--dark);color:#e8e8e8;font-size:11px;display:flex;align-items:center;padding:0 48px;justify-content:space-between}
.topbar .item{display:flex;align-items:center;gap:8px}
.topbar .right{display:flex;gap:40px}
.topbar svg{width:14px;height:14px}
.header{height:92px;display:flex;align-items:center;justify-content:space-between;padding:0 48px;border-bottom:1px solid var(--line)}
.brand{display:flex;align-items:center;gap:10px;font-family:"Raleway",sans-serif;font-weight:700;font-size:28px;letter-spacing:1px;color:var(--ink)}
.brand .mark{width:16px;height:16px;background:var(--ink)}
.nav{display:flex;align-items:center;gap:34px;font-family:"Raleway",sans-serif;font-size:12px;font-weight:600;letter-spacing:1px}
.nav a{color:var(--ink);text-decoration:none;padding:8px 0}
.nav a.active{border-bottom:2px solid var(--ink)}
.pay-btn{margin-left:30px;background:var(--teal);color:var(--white);font-family:"Raleway",sans-serif;font-weight:700;font-size:22px;width:130px;height:50px;display:flex;align-items:center;justify-content:center}
.hero{position:relative;height:700px;background:linear-gradient(100deg,#c7bcb2 0%,#a3877a 22%,#d9d3cd 45%,#e9e7e4 70%,#dcdad6 100%)}
.hero-copy{position:absolute;right:48px;top:245px;width:560px;text-align:right}
.hero-copy h1{font-family:"Italianno",cursive;font-weight:400;font-size:60px;line-height:1;color:var(--ink)}
.hero-copy p{margin-top:14px;text-align:left;font-size:13px;line-height:1.55;color:#333;padding-left:20px}
.btn{display:inline-flex;align-items:center;justify-content:center;font-family:"Raleway",sans-serif;font-weight:700;font-size:11px;letter-spacing:1px;color:var(--white);background:var(--dark);height:32px;padding:0 18px}
.hero-copy .btn{margin-top:16px}
.dots{position:absolute;bottom:20px;left:50%;transform:translateX(-50%);display:flex;gap:10px}
.dots span{width:60px;height:5px;background:rgba(0,0,0,.25)}
.dots span.on{background:var(--ink)}
.about{height:320px;display:flex;align-items:center;padding:0 48px;gap:68px}
.about-photo{width:272px;height:220px;background:linear-gradient(135deg,#d8cfc8,#8b6f62 55%,#efece8)}
.about-text{width:760px}
.about-text h2{font-family:"Raleway",sans-serif;font-size:22px;font-weight:700;margin-bottom:14px}
.about-text p{font-size:12px;line-height:1.7;color:var(--muted);margin-bottom:18px}
.booking{background:var(--grey-bg);height:540px;padding:40px 48px 0;position:relative}
.booking-head{display:flex;justify-content:space-between;align-items:center}
.booking-head h2,.section-title{font-family:"Raleway",sans-serif;font-size:26px;font-weight:600}
.tabs{display:flex;gap:26px;font-size:10px;font-weight:600;letter-spacing:.5px;color:var(--muted)}
.tabs span.on{color:var(--teal);border-bottom:1px solid var(--teal)}
.cards{display:flex;justify-content:space-between;margin-top:28px;padding:0 52px}
.card{width:300px;height:430px;background:var(--white);position:relative;padding:22px 22px 0}
.tag{position:absolute;top:0;left:0;background:var(--tag);color:var(--white);font-size:10px;font-weight:600;padding:4px 8px}
.card-photo{width:170px;height:180px;margin:0 auto}
.meta{display:flex;justify-content:space-between;align-items:baseline;margin-top:22px;border-bottom:1px solid var(--line);padding-bottom:6px}
.price{color:var(--teal);font-size:15px}
.dur{font-size:10px;color:var(--muted)}
.card h3{font-family:"Raleway",sans-serif;font-size:16px;font-weight:600;margin-top:12px}
.card p{font-size:10px;color:var(--muted);line-height:1.6;margin-top:8px;height:48px}
.card-actions{display:flex;gap:38px;margin-top:18px}
.card-actions .btn{width:104px;height:36px;gap:8px}
.card-actions .req{background:var(--teal)}
.gallery{padding-top:60px;height:876px - 0}
.section-title{text-align:center}
.gallery-row{display:flex;justify-content:space-between;padding:0 48px;margin-top:48px}
.gallery-row div{width:268px;height:212px}
.reach{position:absolute;top:2052px;left:0;width:1200px;height:260px;background:linear-gradient(180deg,#5f7a8f,#3e5a70);display:flex;align-items:center;justify-content:center}
.reach h2{font-family:"Raleway",sans-serif;font-size:44px;font-weight:400;color:var(--white)}
.contact{position:absolute;top:2340px;left:0;width:1200px;padding:0 76px}
.contact .section-title{padding-bottom:18px;border-bottom:1px solid var(--line)}
.contact-info{display:flex;gap:0;margin-top:26px}
.contact-info .ci{width:524px;display:flex;align-items:center;gap:18px;font-size:13px;color:#444}
.contact-info .ci:last-child{font-size:22px}
.contact-info svg{width:26px;height:26px}
.field-row{display:flex;justify-content:space-between;margin-top:28px}
.field{width:516px;height:38px;border:1px solid var(--line);background:#f6f6f6;font-size:11px;color:var(--muted);padding:10px 12px}
.message{width:100%;height:190px;margin-top:20px;border:1px solid var(--line);background:#f6f6f6;font-size:11px;color:var(--muted);padding:12px}
.send-row{display:flex;justify-content:flex-end;margin-top:22px}
.send-row .btn{width:120px;height:36px;font-size:13px}
.footer{position:absolute;top:2820px;left:0;width:1200px;height:96px;background:var(--darker);color:#cfcfcf;padding:22px 48px;display:flex;justify-content:space-between}
.footer .links{font-size:10px;display:flex;gap:10px}
.footer .copy{font-size:10px;margin-top:10px}
.socials{display:flex;gap:10px}
.socials span{width:28px;height:28px;background:#ececec}
</style>
</head>
<body>
<div class="topbar">
  <div class="item">
    <svg viewBox="0 0 24 24"><path d="M12 2a7 7 0 0 0-7 7c0 5 7 13 7 13s7-8 7-13a7 7 0 0 0-7-7zm0 9.5A2.5 2.5 0 1 1 12 6.5a2.5 2.5 0 0 1 0 5z" fill="#e8e8e8"/></svg>
    Address Line1, Address line2, 12345, Country
  </div>
  <div class="right">
    <div class="item">
      <svg viewBox="0 0 24 24"><rect x="3" y="6" width="18" height="12" fill="none" stroke="#e8e8e8" stroke-width="2"/><path d="M3 6l9 7 9-7" fill="none" stroke="#e8e8e8" stroke-width="2"/></svg>
      Mail Us<br>info@companyname.com
    </div>
    <div class="item">
      <svg viewBox="0 0 24 24"><path d="M6 3l4 1 1 5-2 1a11 11 0 0 0 5 5l1-2 5 1 1 4-3 3C10 21 3 14 3 6z" fill="#e8e8e8"/></svg>
      Call Us<br>+123 456 7890
    </div>
  </div>
</div>

<header class="header">
  <div class="brand"><span class="mark"></span>Tress Radiant</div>
  <nav class="nav">
    <a class="active">HOME</a><a>BIO</a><a>SERVICES</a><a>GALLERY</a><a>CONTACT US</a>
    <span class="pay-btn">quik pae</span>
  </nav>
</header>

<section class="hero" role="img" aria-label="Portrait photo of the stylist with long auburn hair">
  <div class="hero-copy">
    <h1>Tress Radiant from Root to Soul by Marisol H</h1>
    <p>Lorem ipsum dolor sit amet, consectetur adipiscing elit, sed do eiusmod tempor incididunt ut labore et dolore magna aliqua. Ut enim ad minim veniam, quis nostrud exercitation ullamco laboris nisi ut aliquip ex ea commodo consequat.</p>
    <span class="btn">READ MORE</span>
  </div>
  <div class="dots"><span></span><span class="on"></span><span></span></div>
</section>

<section class="about">
  <div class="about-photo" role="img" aria-label="Photo of Marisol with signature"></div>
  <div class="about-text">
    <h2>Tress Radiant from Root to Soul by Marisol H.</h2>
    <p>Marisol specializes in custom extensions, color and healthy hair care. Each appointment begins with a personal consultation so your look fits your lifestyle, texture and goals. Using premium hair and gentle techniques, she creates natural, lasting results in a warm and relaxing studio where every client leaves feeling confident, cared for and truly radiant.</p>
    <span class="btn">READ MORE</span>
  </div>
</section>

<section class="booking">
  <div class="booking-head">
    <h2>Book an Appointment</h2>
    <div class="tabs"><span class="on">HAIR SERVICES</span><span>COLOR SERVICES</span><span>EXTENSIONS</span><span>TREATMENTS</span></div>
  </div>
  <div class="cards">
    <div class="card">
      <span class="tag">15%</span>
      <div class="card-photo" role="img" aria-label="Photo of a cleanse and style result" style="background:linear-gradient(160deg,#e4e4e4,#6b6b6b)"></div>
      <div class="meta"><span class="price">$145 and up</span><span class="dur">1 hr, 20 min</span></div>
      <h3>Cleanse/ Style</h3>
      <p>Lorem ipsum dolor sit amet, consectetur adipiscing elit, sed do eiusmod.</p>
      <div class="card-actions"><span class="btn req">REQUEST</span><span class="btn">MORE</span></div>
    </div>
    <div class="card">
      <span class="tag">15%</span>
      <div class="card-photo" role="img" aria-label="Photo of a custom short cut" style="background:linear-gradient(160deg,#e9e2da,#5a3b2c)"></div>
      <div class="meta"><span class="price">$145 and up</span><span class="dur">1 hr, 20 min</span></div>
      <h3>Custom Cut Design</h3>
      <p>Lorem ipsum dolor sit amet, consectetur adipiscing elit, sed do eiusmod.</p>
      <div class="card-actions"><span class="btn req">REQUEST</span><span class="btn">MORE</span></div>
    </div>
    <div class="card">
      <span class="tag">15%</span>
      <div class="card-photo" role="img" aria-label="Photo of long curly weave" style="background:linear-gradient(160deg,#c08a62,#6a3a22)"></div>
      <div class="meta"><span class="price">$145 and up</span><span class="dur">1 hr, 20 min</span></div>
      <h3>weave curls</h3>
      <p>Lorem ipsum dolor sit amet, consectetur adipiscing elit, sed do eiusmod.</p>
      <div class="card-actions"><span class="btn req">REQUEST</span><span class="btn">MORE</span></div>
    </div>
  </div>
</section>

<section class="gallery">
  <h2 class="section-title">Our Gallery</h2>
  <div class="gallery-row">
    <div role="img" aria-label="Video still of a styled look" style="background:linear-gradient(135deg,#2a2a2a,#8a8a8a)"></div>
    <div role="img" aria-label="Photo of voluminous dark curls" style="background:linear-gradient(135deg,#1e1612,#6b4a38)"></div>
    <div role="img" aria-label="Photo of long wavy auburn hair" style="background:linear-gradient(135deg,#d9cbc0,#8a4a2c)"></div>
    <div role="img" aria-label="Photo of long black curly hair" style="background:linear-gradient(135deg,#3a2a24,#b89a86)"></div>
  </div>
</section>

<section class="reach" role="img" aria-label="Map of the salon location">
  <h2>Reach Us</h2>
</section>

<section class="contact">
  <h2 class="section-title">Contact Us</h2>
  <div class="contact-info">
    <div class="ci"><svg viewBox="0 0 24 24"><rect x="3" y="6" width="18" height="12" fill="#2b2d31"/><path d="M3 6l9 7 9-7" fill="none" stroke="#fff" stroke-width="1.5"/></svg>info@companyname.com</div>
    <div class="ci"><svg viewBox="0 0 24 24"><circle cx="12" cy="12" r="11" fill="none" stroke="#2b2d31" stroke-width="1.5"/><path d="M8 6l3 1 .5 3-1.5 1a7 7 0 0 0 3 3l1-1.5 3 .5 1 3-2 2C10 18 6 14 6 8z" fill="#2b2d31"/></svg>123 456 7890</div>
  </div>
  <div class="field-row"><div class="field">Name</div><div class="field">Name</div></div>
  <div class="message">Message</div>
  <div class="send-row"><span class="btn">SEND</span></div>
</section>

<footer class="footer">
  <div>
    <div class="links"><span>Policies</span>|<span>Privacy</span>|<span>Terms &amp; Conditions</span>|<span>Disclaimer</span>|<span>Site Map</span></div>
    <div class="copy">Copyright © 2016 Company Name. All Rights Reserved.</div>
  </div>
  <div class="socials"><span></span><span></span><span></span></div>
</footer>
</body>
</html>
```